High end business card design for custom homebuilding company

Looking for a high end business card design that is unique and elegant. Can use embossing, foil printing, laser die cutting, or any high end printing technique or high end paper. Will upload current design so you can see the logo and what we are using currently, but we want something more unique and elegant. I included our logo to help with design.

Target Market(s)

High end custom home buyers of $1.5 million plus homes. Also real estate developers of high end communities.

Industry/Entity Type

Business

Contact Information for Business Card

Double sided. We want something very elegant and expensive looking. We are looking to incorporate a combination of perhaps linen paper or a high end paper, with foil stamping or embossing/debossing to make the card look unique, but still elegant. We tend to use blacks and golds, but are open to any ideas. Looking for creative and unique design.

Colors

Designer to choose colors to be used in the design.

Requirements
Must have
• High end, elegant look. Can use foil, embossing, or high end papers like linen. We want to make the card unique and interesting, but elegant and expensive looking.
Nice to have
• I am including just some cards I saw that looked interesting for one reason or another. I like a clean elegant design and like both the clean white style, and the blacks. So not sure if we want a black design or white. Would like to see both.

```html
<!DOCTYPE html>
<html lang="en">
<head>
<meta charset="utf-8">
<title>Ridgeline Custom Homes — Business Card</title>
<link rel="stylesheet" href="https://fonts.googleapis.com/css2?family=Montserrat:wght@300;400;700&display=swap">
<style>
  :root {
    --stage: #d9d4cc;
    --card-pattern: #e4e4e2;
    --panel: #d9d9d6;
    --frame: #f6f6f4;
    --ink: #1e1e1e;
    --ink-soft: #4a4a4a;
    --gold: #d9a521;
  }
  * { box-sizing: border-box; margin: 0; padding: 0; }
  html, body {
    width: 1200px;
    height: 918px;
    overflow: hidden;
    background: var(--stage);
    font-family: "Montserrat", sans-serif;
  }
  .stage {
    width: 1200px;
    height: 918px;
    display: flex;
    align-items: center;
    justify-content: center;
  }
  .business-card {
    position: relative;
    width: 1000px;
    height: 572px;
    background: var(--card-pattern);
    box-shadow: 0 10px 30px rgba(0,0,0,0.18);
  }
  .card-pattern {
    position: absolute;
    inset: 0;
    background: linear-gradient(135deg, #e8e8e6, #dedfdc);
  }
  .card-panel {
    position: absolute;
    left: 80px;
    top: 80px;
    right: 80px;
    bottom: 80px;
    background: var(--panel);
    border: 6px solid var(--frame);
    outline: 2px solid var(--frame);
    outline-offset: 8px;
    display: flex;
    flex-direction: column;
    justify-content: center;
    padding: 0 60px;
  }
  .brand {
    display: flex;
    align-items: center;
    gap: 28px;
    margin-bottom: 34px;
  }
  .brand-dot {
    width: 80px;
    height: 80px;
    border-radius: 50%;
    background: var(--gold);
    flex: none;
  }
  .brand-name {
    color: var(--ink);
    text-transform: uppercase;
    line-height: 1.05;
    font-weight: 400;
  }
  .brand-name .primary {
    display: block;
    font-size: 58px;
    font-weight: 700;
    letter-spacing: 0.16em;
  }
  .brand-name .secondary {
    display: block;
    font-size: 26px;
    font-weight: 400;
    letter-spacing: 0.62em;
    margin-top: 6px;
  }
  .contact {
    color: var(--ink-soft);
    font-size: 16px;
    font-weight: 300;
    letter-spacing: 0.16em;
    text-transform: uppercase;
    line-height: 1.9;
  }
  .contact .sep { margin: 0 10px; }
</style>
</head>
<body>
  <main class="stage">
    <article class="business-card">
      <div class="card-pattern" role="img" aria-label="Blind-embossed geometric key pattern across the card border"></div>
      <section class="card-panel">
        <div class="brand">
          <span class="brand-dot" aria-hidden="true"></span>
          <h1 class="brand-name">
            <span class="primary">Ridgeline</span>
            <span class="secondary">Custom Homes</span>
          </h1>
        </div>
        <div class="contact">
          <p>Alex Morgan<span class="sep">|</span>555.014.2270<span class="sep">|</span>alex.morgan@example.com</p>
          <p>www.ridgelinecustomhome.example</p>
        </div>
      </section>
    </article>
  </main>
</body>
</html>
```